Remote Planning & Scheduling Power Point Presentation

This PP presentation is to help explain what RPS is and its benefits. Need help with a better illustration on slide 3 that explains the process, overall aesthetics, need better images, and cleaner workflow on slide 18. Keep the DEW Logo in the bottom right of each slide. I have included a one-pager and infographic to help. I am still working of verbiage.

Thanks
SL

```html
<!DOCTYPE html>
<html lang="en">
<head>
<meta charset="utf-8">
<title>RPS Flow Process – Remote Planning</title>
<link rel="stylesheet" href="https://fonts.googleapis.com/css2?family=Open+Sans:wght@300;400;600;700&display=swap">
<style>
  :root {
    --brand-blue: #173b93;
    --slate: #4b5563;
    --slate-light: #e9ecf0;
    --navy: #1c2f6b;
    --tick-grey: #aab0b7;
    --logo-tint: #aebdd6;
    --lime: #8dc63f;
    --ink: #1a1a1a;
    --white: #ffffff;
    --page: #ffffff;
  }
  html, body {
    margin: 0;
    padding: 0;
    width: 1095px;
    height: 1200px;
    overflow: hidden;
    background: var(--page);
  }
  .deck {
    display: block;
    width: 1095px;
    height: 1200px;
    font-family: "Open Sans", Arial, sans-serif;
  }
  .slide-card { fill: var(--white); }
  .band-blue { fill: var(--brand-blue); }
  .band-slate { fill: var(--slate); }
  .band-faint { fill: var(--slate-light); }
  .accent-tab { fill: var(--lime); }
  .slide-title { fill: var(--white); font-weight: 300; font-size: 24px; letter-spacing: 0.3px; }
  .step-number { fill: var(--white); font-weight: 300; font-size: 22px; }
  .step-label { fill: var(--white); font-size: 10.5px; font-weight: 400; }
  .step-item { fill: var(--white); font-size: 7.6px; font-weight: 700; }
  .schedule-item { fill: var(--white); font-size: 8.6px; font-weight: 400; }
  .icon-line { fill: none; stroke: var(--white); stroke-width: 1.3; stroke-linecap: round; stroke-linejoin: round; }
  .icon-fill { fill: var(--white); }
  .logo-word { fill: var(--logo-tint); font-weight: 700; font-size: 14px; letter-spacing: 0.5px; }
  .node-label { fill: var(--ink); font-size: 11px; font-weight: 400; }
  .banner-tag { fill: var(--ink); font-size: 13px; font-weight: 700; }
  .check-label { fill: var(--ink); font-size: 8.6px; }
  .connector { fill: none; stroke: var(--navy); stroke-width: 2; stroke-dasharray: 0.5 4; stroke-linecap: round; }
  .connector-end { fill: var(--navy); }
  .device-frame { fill: var(--brand-blue); }
  .device-screen { fill: #eef1f6; }
  .device-stand { fill: var(--navy); }
  .pictogram { fill: var(--navy); }
  .check-badge { fill: var(--tick-grey); }
  .check-mark { fill: none; stroke: var(--white); stroke-width: 1.6; stroke-linecap: round; stroke-linejoin: round; }
</style>
</head>
<body>
<svg class="deck" viewBox="0 0 718 787" preserveAspectRatio="none" xmlns="http://www.w3.org/2000/svg">
  <defs>
    <filter id="card-shadow" x="-5%" y="-5%" width="110%" height="115%">
      <feDropShadow dx="0" dy="2" stdDeviation="3" flood-color="#000" flood-opacity="0.22"/>
    </filter>
  </defs>

  <!-- Slide: RPS Flow Process -->
  <g class="slide slide-flow">
    <rect class="accent-tab" x="610" y="0" width="55" height="18"/>
    <rect class="slide-card" x="28" y="20" width="664" height="372" filter="url(#card-shadow)"/>
    <polygon class="band-faint" points="560,142 695,142 695,392 640,392"/>
    <polygon class="band-blue" points="55,45 515,45 455,142 55,142"/>
    <polygon class="band-slate" points="515,45 695,45 695,142 455,142"/>
    <text class="slide-title" x="97" y="102">RPS Flow Process</text>

    <!-- Step 1 -->
    <g class="flow-step step-onsite">
      <polygon class="band-blue" points="85,200 215,200 246,285 215,370 85,370"/>
      <rect class="band-slate" x="55" y="165" width="185" height="42"/>
      <text class="step-number" x="65" y="195">1</text>
      <path class="icon-line" d="M110 175 v14 M104 183 l6 6 l6 -6 M102 194 h16"/>
      <text class="step-label" x="129" y="192">On Site</text>
      <rect class="icon-fill" x="171" y="175" width="28" height="18" rx="6" role="img" aria-label="group of people icon"/>

      <path class="icon-line" d="M101 216 h2 M106 216 h14 M101 221 h2 M106 221 h14 M101 226 h2 M106 226 h14 M101 231 h2 M106 231 h14"/>
      <text class="step-item" x="126" y="227">Collect  Worklist</text>
      <rect class="icon-fill" x="98" y="250" width="24" height="10" rx="5" role="img" aria-label="binoculars icon"/>
      <text class="step-item" x="130" y="258">Scope Review</text>
      <rect class="icon-fill" x="97" y="279" width="22" height="17" rx="2" role="img" aria-label="document scroll icon"/>
      <text class="step-item" x="126" y="290">Planning Premise</text>
      <path class="icon-line" d="M101 306 h16 v17 h-16 z M101 312 h16 M101 317 h16"/>
      <text class="step-item" x="126" y="318">Data Collection</text>
      <path class="icon-line" d="M100 338 h20 v13 h-20 z M106 338 l2 -3 h4 l2 3"/>
      <circle class="icon-line" cx="110" cy="344.5" r="3.5"/>
      <text class="step-item" x="136" y="346">Field Photos</text>
    </g>

    <!-- Step 2 -->
    <g class="flow-step step-remote">
      <polygon class="band-blue" points="276,200 440,200 470,285 440,370 276,370 306,285"/>
      <rect class="band-slate" x="253" y="165" width="177" height="42"/>
      <text class="step-number" x="262" y="195">2</text>
      <circle class="icon-fill" cx="307" cy="186" r="2"/>
      <path class="icon-line" d="M302 181 a7 7 0 0 0 0 10 M312 181 a7 7 0 0 1 0 10 M298 178 a12 12 0 0 0 0 16 M316 178 a12 12 0 0 1 0 16"/>
      <text class="step-label" x="320" y="191">Remote</text>
      <rect class="icon-fill" x="373" y="176" width="28" height="18" rx="6" role="img" aria-label="group of people icon"/>

      <circle class="icon-line" cx="320" cy="228" r="3"/>
      <circle class="icon-line" cx="312" cy="221" r="2.5"/>
      <circle class="icon-line" cx="330" cy="221" r="2.5"/>
      <circle class="icon-line" cx="312" cy="236" r="2.5"/>
      <circle class="icon-line" cx="330" cy="236" r="2.5"/>
      <path class="icon-line" d="M314 223 l4 3 M328 223 l-4 3 M314 234 l4 -3 M328 234 l-4 -3"/>
      <text class="step-item" x="348" y="232">Detail Planning</text>
      <circle class="icon-fill" cx="337" cy="264" r="8"/>
      <circle cx="337" cy="264" r="3.5" fill="var(--brand-blue)"/>
      <text class="step-item" x="357" y="267">Develop Package</text>
      <path class="icon-line" d="M318 288 h18 v14 h-18 z M321 293 h8 M321 297 h6"/>
      <circle class="icon-line" cx="336" cy="301" r="3"/>
      <text class="step-item" x="357" y="300">Package Review</text>
      <path class="icon-line" d="M305 333 l8 -6 l6 4 l6 -4 l8 6 M310 338 l5 4 l4 -3 l4 3 l6 -5"/>
      <text class="step-item" x="330" y="342">Package Acceptance</text>
    </g>

    <!-- Step 3 -->
    <g class="flow-step step-schedule">
      <polygon class="band-blue" points="487,200 615,200 645,285 615,370 487,370 517,285"/>
      <rect class="band-slate" x="453" y="165" width="177" height="42"/>
      <text class="step-number" x="470" y="195">3</text>
      <g class="calendar-icon">
        <rect class="icon-line" x="510" y="176" width="20" height="17"/>
        <path class="icon-line" d="M510 181 h20 M513 185 h3 M518 185 h3 M523 185 h3 M513 189 h3 M518 189 h3 M523 189 h3"/>
      </g>
      <text class="schedule-item" x="539" y="183">Level 1</text>
      <text class="schedule-item" x="539" y="196">Schedule</text>

      <text class="schedule-item" x="534" y="220">Schedule Review</text>

      <g class="calendar-icon">
        <rect class="icon-line" x="536" y="243" width="20" height="17"/>
        <path class="icon-line" d="M536 248 h20 M539 252 h3 M544 252 h3 M549 252 h3 M539 256 h3 M544 256 h3 M549 256 h3"/>
      </g>
      <text class="schedule-item" x="565" y="249">Level 2</text>
      <text class="schedule-item" x="565" y="262">Schedule</text>

      <text class="schedule-item" x="540" y="294">Schedule Review</text>

      <g class="calendar-icon">
        <rect class="icon-line" x="522" y="314" width="20" height="17"/>
        <path class="icon-line" d="M522 319 h20 M525 323 h3 M530 323 h3 M535 323 h3 M525 327 h3 M530 327 h3 M535 327 h3"/>
      </g>
      <text class="schedule-item" x="551" y="320">Level 3</text>
      <text class="schedule-item" x="551" y="333">Schedule</text>
    </g>

    <text class="logo-word" x="640" y="371">DEW</text>
  </g>

  <!-- Slide: Keeping Everyone Connected -->
  <g class="slide slide-connected">
    <rect class="slide-card" x="28" y="418" width="664" height="369" filter="url(#card-shadow)"/>
    <polygon class="band-faint" points="600,537 695,537 695,787 680,787"/>
    <polygon class="band-blue" points="55,443 540,443 460,537 55,537"/>
    <polygon class="band-slate" points="540,443 695,443 695,537 460,537"/>
    <polygon fill="#5d6774" points="600,490 695,490 695,537 560,537"/>
    <text class="slide-title" x="98" y="500">Keeping Everyone Connected</text>
    <text class="banner-tag" x="503" y="513">Remote Planning</text>

    <!-- Node labels -->
    <text class="node-label" x="113" y="563">Leadership Team</text>
    <text class="node-label" x="330" y="563">On Site Planner</text>
    <text class="node-label" x="517" y="554">Complete Work</text>
    <text class="node-label" x="539" y="569">Package</text>
    <text class="node-label" x="458" y="696">Remote</text>
    <text class="node-label" x="442" y="711">Planner Team</text>
    <text class="node-label" x="257" y="697">PlanDeck</text>

    <!-- Connectors -->
    <path class="connector" d="M178 578 H298"/>
    <path class="connector" d="M178 594 H298"/>
    <circle class="connector-end" cx="298" cy="578" r="2.6"/>
    <circle class="connector-end" cx="298" cy="594" r="2.6"/>
    <path class="connector" d="M447 615 H535"/>
    <circle class="connector-end" cx="449" cy="615" r="2.6"/>
    <path class="connector" d="M375 668 V688 H337 V698"/>
    <path class="connector" d="M563 670 V740 H520"/>
    <circle class="connector-end" cx="563" cy="680" r="2.6"/>
    <path class="connector" d="M336 737 H438"/>
    <circle class="connector-end" cx="437" cy="737" r="2.6"/>
    <path class="connector" d="M152 612 C152 650, 175 690, 248 730"/>

    <!-- Leadership pictogram -->
    <rect class="pictogram" x="140" y="567" width="38" height="43" rx="14" role="img" aria-label="head silhouette with a brain, representing the leadership team"/>

    <!-- On-site laptop -->
    <rect class="device-frame" x="283" y="572" width="162" height="92" rx="6"/>
    <rect class="device-screen" x="291" y="579" width="146" height="77" role="img" aria-label="planner screen listing open jobs"/>
    <path class="device-stand" d="M270 664 H458 L450 672 H278 Z"/>

    <!-- Work package phone -->
    <rect class="device-frame" x="537" y="574" width="54" height="96" rx="7"/>
    <rect class="device-screen" x="541" y="582" width="46" height="78" role="img" aria-label="phone screen showing a completed work package"/>

    <!-- Desktop monitor -->
    <rect class="device-frame" x="252" y="700" width="84" height="58" rx="4"/>
    <rect class="device-screen" x="256" y="704" width="76" height="48" role="img" aria-label="planning dashboard with charts"/>
    <path class="device-stand" d="M287 758 H301 L304 768 H284 Z"/>

    <!-- Remote team pictogram -->
    <rect class="pictogram" x="440" y="716" width="78" height="36" rx="10" role="img" aria-label="group of remote planners wearing headsets"/>

    <!-- Leadership checklist -->
    <g class="checklist">
      <text class="check-label" x="69" y="636">Monitor Progress</text>
      <circle class="check-badge" cx="157" cy="634" r="9"/>
      <path class="check-mark" d="M153 634 l3 3 l5 -6"/>

      <text class="check-label" x="78" y="665">Review Content</text>
      <circle class="check-badge" cx="168" cy="662" r="9"/>
      <path class="check-mark" d="M164 662 l3 3 l5 -6"/>

      <text class="check-label" x="88" y="689">Develop Budgets</text>
      <circle class="check-badge" cx="182" cy="685" r="9"/>
      <path class="check-mark" d="M178 685 l3 3 l5 -6"/>

      <text class="check-label" x="86" y="713">Track FEL Assignments</text>
      <circle class="check-badge" cx="205" cy="710" r="9"/>
      <path class="check-mark" d="M201 710 l3 3 l5 -6"/>

      <text class="check-label" x="110" y="733">Share with Stakeholders</text>
      <circle class="check-badge" cx="236" cy="728" r="9"/>
      <path class="check-mark" d="M232 728 l3 3 l5 -6"/>
    </g>

    <text class="logo-word" x="645" y="765">DEW</text>
  </g>
</svg>
</body>
</html>
```